Business cards design for T38 (Разработка визитных карточек)

We would like to get design of our business cards loosely based on our website design [url removed, login to view]

logo in vector is atteched

There should be following info to be present on business card:
Martin Colvey
CEO
T38
+7 (222) 222-22-22
+7 (222) 222-22-22
colvey@tessarine-mail.ru
222222, Moscow, Ulitsa Tikhvoronskaya, 7B

```html
<!DOCTYPE html>
<html lang="en">
<head>
<meta charset="utf-8">
<title>T38 business cards</title>
<link href="https://fonts.googleapis.com/css2?family=PT+Sans:wght@400;700&display=swap" rel="stylesheet">
<style>
  :root {
    --bg: #e9e6e1;
    --red: #d3121b;
    --red-dark: #a80d14;
    --red-light: #e0222a;
    --white: #ffffff;
    --paper: #f4f4f4;
    --ink: #3a3a3a;
    --ink-soft: #6b6b6b;
    --rule: #c9c9c9;
    --black: #1c1c1c;
    --placeholder: #d6d6d6;
  }
  * { margin: 0; padding: 0; box-sizing: border-box; }
  html, body {
    width: 1200px; height: 1041px; overflow: hidden;
    background: var(--bg);
    font-family: "PT Sans", Arial, sans-serif;
  }
  .sheet {
    width: 1200px; height: 1041px;
    display: flex; flex-direction: column;
    align-items: center; justify-content: center; gap: 60px;
  }
  .card {
    position: relative;
    width: 760px; height: 434px;
    border-radius: 4px;
    box-shadow: 0 6px 18px rgba(0,0,0,.18);
    overflow: hidden;
  }
  /* front */
  .card--front {
    background: linear-gradient(135deg, var(--red-light) 0%, var(--red) 45%, var(--red-dark) 100%);
    color: var(--white);
  }
  .front-logo {
    position: absolute; left: 70px; top: 120px;
    font-weight: 700; font-size: 170px; line-height: 1; letter-spacing: 4px;
  }
  .front-address {
    position: absolute; left: 74px; bottom: 72px;
    font-size: 20px; line-height: 1.2;
  }
  .front-web {
    position: absolute; right: 54px; bottom: 72px;
    font-size: 20px; line-height: 1.2;
  }
  /* back */
  .card--back {
    background: linear-gradient(160deg, var(--white) 0%, var(--paper) 100%);
    color: var(--ink);
  }
  .knob-placeholder {
    position: absolute; left: 64px; top: 54px;
    width: 252px; height: 252px; border-radius: 50%;
    background: var(--placeholder);
  }
  .identity {
    position: absolute; right: 56px; top: 60px; width: 330px;
    text-align: right;
  }
  .back-logo {
    font-weight: 700; font-size: 72px; line-height: 1; color: var(--red);
    letter-spacing: 2px;
  }
  .person-name { margin-top: 14px; font-size: 26px; line-height: 1.2; color: var(--ink); }
  .person-role { font-size: 20px; line-height: 1.2; color: var(--red); }
  .divider { margin: 14px 0 16px auto; width: 260px; height: 1px; background: var(--rule); }
  .contacts { list-style: none; }
  .contacts li {
    display: flex; justify-content: flex-end; align-items: center; gap: 10px;
    font-size: 17px; line-height: 26px; color: var(--ink-soft);
    white-space: nowrap;
  }
  .contacts svg { width: 14px; height: 14px; flex: none; }
  .edge-stripe {
    position: absolute; left: 0; right: 0; bottom: 30px; height: 3px;
    display: flex;
  }
  .edge-stripe .dark { flex: 1; background: var(--black); }
  .edge-stripe .accent { flex: 1; background: var(--red); }
</style>
</head>
<body>
<main class="sheet">

  <section class="card card--front">
    <div class="front-logo">T38</div>
    <p class="front-address">222222, Moscow, Ulitsa Tikhvoronskaya, 7B</p>
    <p class="front-web">www.t38studio.ru</p>
  </section>

  <section class="card card--back">
    <div class="knob-placeholder" role="img" aria-label="Illustration of a metal control knob"></div>

    <div class="identity">
      <div class="back-logo">T38</div>
      <p class="person-name">Martin Colvey</p>
      <p class="person-role">CEO</p>
      <div class="divider"></div>
      <ul class="contacts">
        <li>+7 (222) 222-22-22
          <svg viewBox="0 0 14 14"><path d="M3 1l3 3-1.5 1.5a8 8 0 0 0 4 4L10 8l3 3-2 2C6 13 1 8 1 3z" fill="var(--red)"/></svg></li>
        <li>+7 (222) 222-22-22
          <svg viewBox="0 0 14 14"><path d="M3 1l3 3-1.5 1.5a8 8 0 0 0 4 4L10 8l3 3-2 2C6 13 1 8 1 3z" fill="var(--red)"/></svg></li>
        <li>colvey@tessarine-mail.ru
          <svg viewBox="0 0 14 14"><rect x="1" y="3" width="12" height="8" fill="var(--red)"/><path d="M1 3l6 5 6-5" stroke="#fff" fill="none"/></svg></li>
        <li>www.t38studio.ru
          <svg viewBox="0 0 14 14"><circle cx="7" cy="7" r="5.5" fill="none" stroke="var(--red)" stroke-width="1.6"/></svg></li>
      </ul>
    </div>

    <div class="edge-stripe"><span class="dark"></span><span class="accent"></span></div>
  </section>

</main>
</body>
</html>
```